ECommerce Site Redesign: overall site and specific pages

We have a website that has been in operation for 6+ years, and it's time for a visual refresh.

Our current website is located at http://trk.example

The only significant functional change will be the movement of the persistent vertical navigation bar from the left side up to a categorized horizontal navigation menu. I've attached a rough mockup of how we want this positioned.

No coding necessary; just PSDs. The attached ROUGH MENU MOCKUP.PSD contains a layer with our logo on white should you wish to include it in your submissions.

Target Market(s)

We are an outdoor retailer focused on the high end of the market. We have a general color scheme on our site which we'd like to keep, but various elements need to be made consistent and more aesthetically pleasing.

Our brand is very important to us, and the site design must reflect our values of high quality and affluence. We cater to outdoor enthusiasts, hikers, back packers, and general high end apparel consumers.

Requirements
Must have
• In order to address the issue of consistency, we require strict design guidelines, including font sizing, element spacing, etc.

We require 7 page design templates for:

1.) overall site template - see http://trk.example for current.
* narrow static header bar (NEW)
* footer (KEEP SAME/SIMILAR)
* background
* body
* mini-cart (collapsed and expanded)
* promotion panel (ad box, rotating featured items)
* horizontal navigation bars (expanded/collapsed, grouped by 7 main categories) - see attached ROUGH MENU MOCKUP and see additional notes.
* recently viewed products

2.) product page (see http://trk.example/270599/frostline_summit-cowl-merino-mens.aspx for current)
* product imagery/zoombox
* color, size, quantity selection
* add to cart button
* detail tabs
* In-store Availability info
* info panel near the add to cart box for exceptions including:
- Available to pick up in-store only
- Free shipping for your entire order when you purchase this item
- This item is over-sized; please contact a store directly
* "customers who bought this also bought" panel, grid listing of items

3.) product listings (category, search results, etc.)
* item thumbnails in grid format
* sidebar for refinement options (by supplier, by price, by size, etc.)

4.) generic information/content page (see http://trk.example/t-returns.aspx)

5.) store locations page (see http://trk.example/t-TRK.stores.04.aspx)
* store details
* map
* hours
* contact info
* local links
* contact form

6.) contact us form

7.) checkout (see attached current checkout screen shot)
* cart summary
* checkout steps

Any visual elements benefiting from hover effects will need to have both dimmed and hovered layers in the design.

```html
<!DOCTYPE html>
<html lang="en">
<head>
<meta charset="utf-8">
<title>Ridgeline Peak Outfitters – BackPacks</title>
<link href="https://fonts.googleapis.com/css2?family=Arimo:wght@400;700&family=Gelasio:wght@400&display=swap" rel="stylesheet">
<style>
:root{
  --purple:#8b64ac;
  --purple-dark:#6c3f95;
  --purple-title:#8557a8;
  --link:#1b6fc0;
  --text:#333;
  --sky:#b9d8ee;
  --page:#ececec;
  --footer-line:#2b72c4;
  --white:#fff;
}
*{box-sizing:border-box;margin:0;padding:0}
html,body{width:1025px;height:1200px;overflow:hidden}
body{font-family:Arimo,Arial,sans-serif;color:var(--text);background:linear-gradient(#fff 330px,var(--page) 900px);position:relative}
a{color:inherit;text-decoration:none}
.abs{position:absolute}

/* top bar */
.topbar{left:0;top:0;width:1025px;height:46px;background:var(--purple);color:var(--white);font-size:12px}
.topbar .links{left:128px;top:20px}
.topbar .cart{right:199px;top:19px;white-space:nowrap}
.checkout{left:833px;top:15px;width:77px;height:22px;border-radius:4px;background:linear-gradient(#6fc2f3,#2a8fd4);font-weight:700;font-size:11px;text-align:center;line-height:22px;color:#fff}

/* header */
.header{left:0;top:46px;width:1025px;height:134px;background:linear-gradient(#fff 30px,var(--sky))}
.logo{left:124px;top:64px;font-family:Gelasio,Georgia,serif;font-size:30px;color:var(--purple-dark);letter-spacing:1px;line-height:1}
.logo small{display:block;font-size:10px;letter-spacing:11px;margin-top:4px;padding-left:48px}
.search{left:656px;top:66px;width:255px;height:28px;border:1px solid #bbb;border-radius:4px;background:#fff;font-size:10px;font-style:italic;color:#aaa;padding:8px 8px}
.search-btn{left:882px;top:66px;width:29px;height:28px;border-radius:0 4px 4px 0;background:linear-gradient(#6fc2f3,#2a8fd4)}
.nav{left:130px;top:146px;width:770px;display:flex;justify-content:space-between;font-size:13.5px;color:#111}
.nav span.sep{color:#333}
.nav-line{left:135px;top:167px;width:765px;height:2px;background:linear-gradient(90deg,transparent,#8aa9c0,transparent)}
.hero{left:0;top:180px;width:1025px;height:143px;background:linear-gradient(#7c98b5,#d8e0e8 45%,#eef0f2 70%,#aab3bc)}

/* sidebar */
.sidebar{left:128px;top:348px;width:199px;height:527px;border-radius:12px;background:linear-gradient(#fff 60%,var(--sky) 70%);box-shadow:0 1px 5px rgba(0,0,0,.35)}
.cats{left:122px;top:365px;width:196px;list-style:none}
.cats li{height:28px;margin-bottom:5.5px;background:var(--purple);color:#fff;display:flex;justify-content:space-between;align-items:center;padding:0 24px 0 23px;font-family:Gelasio,Georgia,serif;font-size:15px}
.cats li span{font-family:Arimo,Arial,sans-serif;font-size:11px}
.cats li.active{box-shadow:inset 0 0 0 8px var(--purple);background:#b79ccc;color:#111}
.chat{left:130px;top:607px;width:196px;height:208px;background:linear-gradient(160deg,#9ab8cc,#4d6474 55%,#1e2428)}
.chat-text{left:136px;top:722px;color:#fff;font-size:22px;line-height:1.3}
.chat-text .off{color:#e6a545;font-size:21px}
.chat-text .sub{font-size:15px}

/* content */
.title{left:352px;top:352px;font-size:25px;font-weight:700;color:var(--purple-title)}
.title-icon{left:490px;top:342px}
.intro{left:353px;top:386px;width:558px;font-size:11.7px;line-height:17.6px;color:#444}
.brands{left:345px;top:508px;width:566px;height:67px;border:3px solid #ccc;border-radius:12px;background:#fff;display:flex;align-items:center;justify-content:space-around;padding:0 30px;font-size:11px;font-weight:700;color:#222}
.brands .arrow{position:absolute;top:12px;font-size:34px;color:#ccc;font-weight:400}
.subnav{left:345px;top:612px;width:152px;list-style:none}
.subnav li{height:24px;border-bottom:1px dotted #bbb;font-size:13px;color:var(--link);line-height:24px}
.subnav li::before{content:"»";font-size:10px;color:#777;margin-right:6px}
.card{width:87px;height:131px;border-radius:7px;background:#fff;box-shadow:0 0 3px rgba(0,0,0,.35);overflow:hidden}
.card .pic{height:92px;margin:8px 14px 0;border-radius:4px}
.card .info{position:absolute;bottom:0;left:0;right:0;height:40px;background:var(--purple);color:#fff;font-size:10.5px;text-align:center;line-height:15px;padding-top:4px}

/* footer */
.footer{left:0;top:907px;width:1025px;height:293px;background:var(--purple);border-top:3px solid var(--footer-line);color:#fff;font-size:10.5px}
.f-logo{left:124px;top:940px;font-family:Gelasio,Georgia,serif;font-size:26px;color:var(--purple-dark);line-height:1}
.f-logo small{display:block;font-size:8px;letter-spacing:10px;padding-left:40px;margin-top:2px}
.social{left:130px;color:#fff;font-size:10.5px;display:flex;gap:6px;align-items:center;line-height:13px}
.social i{display:block;width:29px;height:29px;border-radius:3px;background:#4a5fa5}
.fcol{color:#fff;font-size:10.5px;line-height:19.2px;letter-spacing:.3px}
.fcol h4{font-weight:400;font-size:11px;margin-bottom:4px}
.copy{left:0;width:1025px;top:1174px;text-align:center;font-size:10.5px;color:#e6dcef}
</style>
</head>
<body>
<header>
  <div class="abs topbar">
    <div class="abs links">FIND A STORE &nbsp; | &nbsp;CONTACT US &nbsp;| &nbsp;Ph.888-555-0142</div>
    <div class="abs cart">There are &nbsp;items in your cart. $0.00</div>
  </div>
  <a class="abs checkout" href="#">CHECKOUT</a>
  <div class="abs header"></div>
  <div class="abs logo">RIDGELINE PEAK<small>OUTFITTERS</small></div>
  <div class="abs search">serch entire store here...</div>
  <div class="abs search-btn">
    <svg width="29" height="28" viewBox="0 0 29 28"><circle cx="16" cy="12" r="6" fill="none" stroke="#fff" stroke-width="2.5"/><line x1="11.5" y1="16.5" x2="7" y2="21" stroke="#fff" stroke-width="3"/></svg>
  </div>
  <nav class="abs nav">
    <a href="#">Home</a><span class="sep">|</span><a href="#">Women</a><span class="sep">|</span><a href="#">Men</a><span class="sep">|</span><a href="#">Gears</a><span class="sep">|</span><a href="#">Ultralight</a><span class="sep">|</span><a href="#">Inspire</a><span class="sep">|</span><a href="#">Reviews</a><span class="sep">|</span><a href="#">On Sale</a>
  </nav>
  <div class="abs nav-line"></div>
  <div class="abs hero" role="img" aria-label="Two hikers with trekking poles standing on a rocky summit above a sea of clouds"></div>
</header>

<aside>
  <div class="abs sidebar"></div>
  <ul class="abs cats">
    <li>Sunglasses<span>113</span></li>
    <li class="active">BackPacks<span>36</span></li>
    <li>Hydration<span>395</span></li>
    <li>Tents &amp; Traps<span>53</span></li>
    <li>Sleeping Bags<span>88</span></li>
    <li>Camp Kitchen<span>34</span></li>
    <li>Rops &amp; Cordage<span>93</span></li>
  </ul>
  <div class="abs chat" role="img" aria-label="Silhouettes of climbers helping each other up a rock against a bright sky"></div>
  <div class="abs chat-text">LIVE CHAT<br><span class="off">Currently Offline</span><br><span class="sub">click to send a message</span></div>
</aside>

<main>
  <h1 class="abs title">BackPacks</h1>
  <svg class="abs title-icon" width="30" height="36" viewBox="0 0 30 36"><rect x="5" y="6" width="20" height="26" rx="8" fill="#8a4fb0"/><rect x="9" y="18" width="12" height="10" rx="3" fill="#b07fd0"/><path d="M10 7 Q15 0 20 7" fill="none" stroke="#8a4fb0" stroke-width="2"/></svg>
  <p class="abs intro">Lorem ipsum dolor sit amet, consectetur adipiscing elit. Aliquam semper ligula a arcu rutrum sit amet imperdiet tellus viverra. Vestibulum ante ipsum primis in faucibus orci luctus et ultrices posuere cubilia Curae; Vivamus sapien turpis, sodales sed placerat vel, iaculis ut lorem. Curabitur at tempor mauris. Nulla in rutrum sem. Fusce ultrices tortor id risus ullamcorper sed placerat sem dignissim. Fusce faucibus turpis sed dui cursus congue vel vitae diam. Proin pharetra commodo ligula eu bibendum. Quisque vitae dui vitae urna fringilla tempor eget eu odio. Curabitur tincidunt augue vel.</p>

  <div class="abs brands">
    <span class="arrow" style="left:8px">(</span>
    <span>Northcrest</span><span>Alpwerk</span><span>Tidecline</span><span>Harrowfin</span><span>Burrowfield</span><span>Slate Summit</span>
    <span class="arrow" style="right:8px">)</span>
  </div>

  <ul class="abs subnav">
    <li>Day Packs</li><li>Packs Over 4oL</li><li>Travel Bags</li><li>Lumbar Packs</li><li>Backpack Accessories</li><li>Child Carriers</li>
  </ul>

  <div class="abs card" style="left:525px;top:595px"><div class="pic" role="img" aria-label="Black backpack" style="background:radial-gradient(#555,#222 60%,#fff 61%)"></div><div class="info">$99.95(CAD)<br>Crest blade</div></div>
  <div class="abs card" style="left:623px;top:595px"><div class="pic" role="img" aria-label="Dark teal backpack" style="background:radial-gradient(#3b5a62,#1f3439 60%,#fff 61%)"></div><div class="info">$99.95(CAD)<br>Crest blade</div></div>
  <div class="abs card" style="left:721px;top:595px"><div class="pic" role="img" aria-label="Grey and red backpack" style="background:radial-gradient(#b22a3a,#444 60%,#fff 61%)"></div><div class="info">$99.95(CAD)<br>Crest blade</div></div>
  <div class="abs card" style="left:818px;top:595px"><div class="pic" role="img" aria-label="Orange backpack" style="background:radial-gradient(#f36a2a,#d9400f 60%,#fff 61%)"></div><div class="info">$99.95(CAD)<br>Crest blade</div></div>
  <div class="abs card" style="left:525px;top:749px"><div class="pic" role="img" aria-label="Blue backpack" style="background:radial-gradient(#3d9be6,#1561b2 60%,#fff 61%)"></div><div class="info">$99.95(CAD)<br>Crest blade</div></div>
  <div class="abs card" style="left:623px;top:749px"><div class="pic" role="img" aria-label="Black pack with rain cover" style="background:radial-gradient(#444,#151515 60%,#fff 61%)"></div><div class="info">$99.95(CAD)<br>Crest blade</div></div>
  <div class="abs card" style="left:721px;top:749px"><div class="pic" role="img" aria-label="Green messenger bag" style="background:radial-gradient(#6ccf3a,#36a020 60%,#fff 61%)"></div><div class="info">$99.95(CAD)<br>Crest blade</div></div>
  <div class="abs card" style="left:818px;top:749px"><div class="pic" role="img" aria-label="Yellow backpack" style="background:radial-gradient(#f3e03a,#c6b515 60%,#fff 61%)"></div><div class="info">$99.95(CAD)<br>Crest blade</div></div>
</main>

<footer>
  <div class="abs footer"></div>
  <div class="abs f-logo">RIDGELINE PEAK<small>OUTFITTERS</small></div>
  <div class="abs social" style="top:989px"><i></i><span>Ridgeline Peak Outfitters on<br>Friendspace</span></div>
  <div class="abs social" style="top:1032px"><i style="background:#9aa0a8"></i><span>Message from our President</span></div>
  <div class="abs social" style="top:1074px"><i style="background:#3e62b0"></i><span>Email our president</span></div>

  <div class="abs fcol" style="left:390px;top:976px"><h4>Ridgeline Peak Stores</h4></div>
  <div class="abs fcol" style="left:398px;top:999px">Thornvale<br>Larchmere<br>Quillby<br>Ravenmoor Flats<br>Stonewell<br>Elkhollow</div>
  <div class="abs fcol" style="left:518px;top:999px">Mossbury<br>Pinecastle<br>Wyndcrest<br>Ashgrove<br>Fernholt<br>Tamarack Bay</div>
  <div class="abs fcol" style="left:380px;top:1119px;font-style:italic">Each shop is locally owned and operated</div>
  <div class="abs fcol" style="left:638px;top:976px"><h4>Site Services</h4></div>
  <div class="abs fcol" style="left:640px;top:999px">Privacy and<br>Security<br>Return Policy<br>Shipping Rates<br>Terms &amp;<br>Conditions<br>Site Map</div>
  <div class="abs fcol" style="left:767px;top:976px"><h4>About RPO</h4></div>
  <div class="abs fcol" style="left:768px;top:990px">About Us<br>Frequently Asked<br>Questions<br>Contact Us</div>
  <div class="abs fcol" style="left:767px;top:1074px"><h4>My RPO</h4></div>
  <div class="abs fcol" style="left:768px;top:1089px">My RPO Account<br>Info<br>My Address<br>Change</div>
  <div class="abs copy">(C) 2012 Ridgeline Peak Outfitters Inc. ALL RIGHTS RESERVED</div>
</footer>
</body>
</html>
```